Business Card Design Project - Customized Posters

The project is to design a business card for a new web based company, that designs customized posters celebrating all types of special occasions including birthdays, weddings, new born babys, special memories etc.

You are free to design whatever you want - the only stipulation is the card truly reflects our website and our products. It's preferable that the logo is included (though not essential) and there will be one name and telephone number on the card (use A.N.Other as the name and 0123 456789 as the number) as well as our website address and email. The card should be double sided.

Our website is www.copperwaveco.com.au - you will get a complete picture of what we do and hopefully plenty of inspiration for the business card!

Any questions please email sales@copperwaveco.com.au and I'll respond asap. Thanks and good luck!

Target Market(s)

Everyone that would be interested in buying one of our posters!

Industry/Entity Type

Business

Requirements
Must have
• Our website address
Our email address
One name and telephone number
Nice to have
• Our logo
Should not have
• Physical address

```html
<!DOCTYPE html>
<html lang="en">
<head>
<meta charset="utf-8">
<title>Copperwave Co – Business Card</title>
<link rel="stylesheet" href="https://fonts.googleapis.com/css2?family=Russo+One&family=Michroma&display=swap">
<style>
  :root {
    --bg: #e6e6e6;
    --card: #1b1b1b;
    --white: #ffffff;
    --purple: #7e2f8f;
    --green: #0ba24b;
    --blue: #2e3182;
    --red: #e3202a;
    --orange: #f28c1c;
    --cyan: #29abe2;
    --head: "Russo One", sans-serif;
    --body: "Michroma", sans-serif;
  }
  * { box-sizing: border-box; margin: 0; padding: 0; }
  html, body { width: 1200px; height: 874px; overflow: hidden; background: var(--bg); }
  .canvas { position: relative; width: 1200px; height: 874px; }

  .card { position: absolute; background: var(--card); overflow: hidden; box-shadow: 0 6px 18px rgba(0,0,0,.25); }
  .card--front { left: 110px; top: 147px; width: 340px; height: 580px; }
  .card--back  { left: 510px; top: 267px; width: 580px; height: 340px; }

  .colour-field {
    position: absolute;
    background: linear-gradient(135deg, var(--purple) 0%, var(--blue) 40%, var(--red) 75%, var(--orange) 100%);
    opacity: .9;
  }
  .colour-field--front-top    { left: 20px; top: 0;     width: 300px; height: 72px; }
  .colour-field--front-middle { left: 20px; top: 290px; width: 300px; height: 54px; }
  .colour-field--front-bottom { left: 20px; top: 500px; width: 300px; height: 60px; }
  .colour-field--back         { left: 20px; top: 14px;  width: 300px; height: 286px; }

  .brand { position: absolute; left: 30px; top: 170px; display: flex; align-items: center; gap: 12px; }
  .brand__mark { width: 24px; height: 24px; background: var(--white); }
  .brand__name { font-family: var(--head); font-size: 24px; color: var(--white); letter-spacing: .5px; }

  .contact { position: absolute; left: 30px; top: 372px; color: var(--white); }
  .contact__name { font-family: var(--head); font-size: 24px; letter-spacing: 1px; margin-bottom: 10px; }
  .contact__first { color: var(--green); }
  .contact__last { color: var(--red); }
  .contact__line { font-family: var(--body); font-size: 11.5px; line-height: 25px; }

  .tagline { position: absolute; left: 342px; top: 34px; width: 224px; font-family: var(--head); font-weight: 400; color: var(--white); line-height: 1.04; }
  .tagline span { display: block; white-space: nowrap; }
  .tagline__brand { font-size: 23px; }
  .tagline__the { font-size: 34px; }
  .tagline__accent { font-size: 29px; color: var(--cyan); }
  .tagline__idea { font-size: 38px; }
  .tagline__for { font-size: 25px; }
  .tagline__occasion { font-size: 30px; }

  .back-url { position: absolute; left: 22px; bottom: 14px; font-family: var(--body); font-size: 12px; color: var(--white); }
</style>
</head>
<body>
<main class="canvas">

  <section class="card card--front" aria-label="Business card front">
    <div class="colour-field colour-field--front-top" role="img" aria-label="Decorative band of coloured blocks"></div>

    <div class="brand">
      <span class="brand__mark"></span>
      <span class="brand__name">COPPERWAVE CO</span>
    </div>

    <div class="colour-field colour-field--front-middle" role="img" aria-label="Decorative band of coloured blocks"></div>

    <div class="contact">
      <p class="contact__name"><span class="contact__first">TESS</span> <span class="contact__last">MARLOW</span></p>
      <p class="contact__line">0400 123 987</p>
      <p class="contact__line">sales@copperwaveco.com.au</p>
      <p class="contact__line">www.copperwaveco.com.au</p>
    </div>

    <div class="colour-field colour-field--front-bottom" role="img" aria-label="Decorative band of coloured blocks"></div>
  </section>

  <section class="card card--back" aria-label="Business card back">
    <div class="colour-field colour-field--back" role="img" aria-label="Decorative field of coloured blocks"></div>

    <h2 class="tagline">
      <span class="tagline__brand">COPPERWAVE CO</span>
      <span class="tagline__the">THE</span>
      <span class="tagline__accent">PERFECT GIFT</span>
      <span class="tagline__idea">IDEA</span>
      <span class="tagline__for">FOR ANY</span>
      <span class="tagline__occasion">OCCASION!</span>
    </h2>

    <p class="back-url">www.copperwaveco.com.au</p>
  </section>

</main>
</body>
</html>
```